Business Card Design Project

We need a business card design for a new construction company called 'KVORA HOLDINGS PTY.LTD' We run a construction based company for high end market homes in melbourne, we want something that looks professional and eye catching.The card needs to have a strong design to it something modern as the company name explains "kvora." The final design should communicate professionalism and a strong image to our customers on the quality of our work.
On the business card i need
Name: Marek Tollaway
Mob:0417295041
Email:kvora.holdings@mailbrook.example
Domestic/Residential/Commercial
Industry/Entity Type
Construction
Look and feel
Each slider illustrates characteristics of the customer's brand and the style your logo design should communicate.

```html
<!DOCTYPE html>
<html lang="en">
<head>
<meta charset="UTF-8">
<title>KVORA HOLDINGS PTY.LTD — Business Card</title>
<link rel="stylesheet" href="https://fonts.googleapis.com/css2?family=Ubuntu:wght@300;400;500;700&display=swap">
<style>
  :root {
    --page-bg: #e9e7e4;
    --brand-red: #e21d3c;
    --brand-red-light: #ee3d58;
    --card-white: #f4f4f4;
    --ink-dark: #2b2b2b;
    --ink-white: #ffffff;
  }
  * { box-sizing: border-box; margin: 0; padding: 0; }
  html, body {
    width: 1200px;
    height: 900px;
    overflow: hidden;
    background: var(--page-bg);
    font-family: "Ubuntu", sans-serif;
  }
  .canvas {
    width: 1200px;
    height: 900px;
    display: flex;
    flex-direction: column;
    align-items: center;
    justify-content: center;
    gap: 56px;
  }
  .card {
    position: relative;
    width: 640px;
    height: 366px;
    overflow: hidden;
    box-shadow: 0 6px 18px rgba(0,0,0,0.18);
  }

  /* Front side */
  .card--front {
    background: linear-gradient(160deg, var(--brand-red) 0%, var(--brand-red-light) 60%, var(--brand-red) 100%);
  }
  .front-corner-strip {
    position: absolute;
    top: 0;
    right: 0;
    width: 180px;
    height: 18px;
    background: var(--card-white);
  }
  .logo-panel {
    position: absolute;
    left: 0;
    top: 28px;
    width: 280px;
    height: 250px;
    background: var(--card-white);
    border-radius: 0 28px 28px 0;
    display: flex;
    flex-direction: column;
    justify-content: center;
    align-items: center;
  }
  .brand {
    display: flex;
    flex-direction: column;
    align-items: center;
  }
  .brand-name {
    display: flex;
    align-items: center;
    gap: 8px;
    color: var(--ink-dark);
    font-weight: 500;
    letter-spacing: -1px;
    line-height: 1;
  }
  .brand-dot {
    border-radius: 50%;
    background: var(--brand-red);
  }
  .brand-tagline {
    color: var(--brand-red);
    font-weight: 400;
    text-transform: uppercase;
    letter-spacing: 0.32em;
  }
  .logo-panel .brand-name { font-size: 62px; }
  .logo-panel .brand-dot { width: 12px; height: 12px; }
  .logo-panel .brand-tagline { font-size: 10px; margin-top: 8px; }

  .contact {
    position: absolute;
    left: 330px;
    top: 92px;
    color: var(--ink-white);
  }
  .contact-name {
    font-size: 20px;
    font-weight: 700;
    margin-bottom: 14px;
  }
  .contact-label {
    font-size: 11px;
    font-weight: 400;
    text-transform: uppercase;
    letter-spacing: 0.04em;
  }
  .contact-phone {
    font-size: 16px;
    font-weight: 300;
    margin-top: 2px;
  }
  .contact-email {
    position: absolute;
    left: 330px;
    bottom: 30px;
    color: var(--ink-white);
    font-size: 14px;
    font-weight: 400;
  }

  /* Back side */
  .card--back {
    background: linear-gradient(135deg, #ffffff 0%, var(--card-white) 55%, #e4e4e4 100%);
    display: flex;
    align-items: center;
    justify-content: center;
  }
  .back-top-bar {
    position: absolute;
    top: 0;
    left: 60px;
    width: 220px;
    height: 16px;
    background: var(--brand-red);
  }
  .card--back .brand-name { font-size: 104px; }
  .card--back .brand-dot { width: 18px; height: 18px; }
  .card--back .brand-tagline { font-size: 14px; margin-top: 10px; }
</style>
</head>
<body>
  <main class="canvas">
    <section class="card card--front" aria-label="Business card front">
      <div class="front-corner-strip"></div>
      <div class="logo-panel">
        <div class="brand">
          <div class="brand-name">kvora<span class="brand-dot"></span></div>
          <div class="brand-tagline">Kvora Holdings Pty.Ltd</div>
        </div>
      </div>
      <div class="contact">
        <p class="contact-name">Marek Tollaway</p>
        <p class="contact-label">Phone</p>
        <p class="contact-phone">0417295041</p>
      </div>
      <p class="contact-email">kvora.holdings@mailbrook.example</p>
    </section>

    <section class="card card--back" aria-label="Business card back">
      <div class="back-top-bar"></div>
      <div class="brand">
        <div class="brand-name">kvora<span class="brand-dot"></span></div>
        <div class="brand-tagline">Kvora Holdings Pty.Ltd</div>
      </div>
    </section>
  </main>
</body>
</html>
```